Cartlyft product design and upload for Coffee Shop

Coffee Shop, Store Front & Online - Cartlyft theme

***Important*** Credentials to complete the gig will only be shared via Keyvaultly or a similar password share application. Please ensure you will be able to do this before proceeding.

Please advise if you have worked with any Cartlyft theme in storewell?

Job Description
Set up and customize all products to Storewell for my Coffee Shop and customize to my colours and brand - using the current installed cartlyft theme.

Hi there, I have a "Physical retail Cafe" I am looking for someone to upload the attached menu for me in the products section of my Storewell store and make the store look and display awesome. Need expert who has a good understanding of the storewell and cartlyft system as I need a quick turn around.

Existing Old site - www.mugamiles.com.au
New storewell site to be set up with cartlyft theme - https://mugamiles.mystorewell.com/

Attached in these excel spreadsheets are the menus:
1.Muga Miles Insotre Menu - Muga Miles Online Shop Menu
2. Muga Miles Online Shop Menu

1. In Store Menu - where customers can only purchase the items in the store - however they will be able to view all items online. So a visually appealing display of products and ease of viewing of the menu is important.
Currently customers can order this menu here - http://tapvia.example/r82kzm using phone app, computer or any device and pick up only from store.

2. Online Shop Menu - They can purchase these items online and we can ship.

Examples provided below of how I would like the sites I like - and would like similar design using our products and items. Please feel free to use your expertise to solve and issues or improve.
Also I am happy to discuss any ideas or questions you have.

We do not have many images of our products at the moment so please free to use any of the images from below sites as a temporary pic - unless you can source some better original ones or have some ideas...

Please see all attachments for full details.

Target Market(s)

Coffee Shop - Retail Store Front & Online

Colors
fffefc
ffffff

Requirements
Must have
• Pleas read attached brief
Nice to have
• Experience using cartlyft theme. Open to using another theme if designer can deisgn style I am looking for as per the examples in the brief.
Should not have
• As per the brieft

```html
<!DOCTYPE html>
<html lang="en">
<head>
<meta charset="utf-8">
<title>Muga Miles – Shop</title>
<link href="https://fonts.googleapis.com/css2?family=Oswald:wght@400;500&family=Nunito:wght@700;800&display=swap" rel="stylesheet">
<style>
:root{
  --red:#ec2027;
  --white:#ffffff;
  --cream:#fffefc;
  --nav-bg:#f1f5f8;
  --lime:#a6cf3a;
  --ink:#2b2b2b;
  --grey-text:#8a8a8a;
  --item:#8c8c8c;
  --dim:#7f7f7f;
  --fb:#1877f2;
  --flag-blue:#1c3f94;
}
*{margin:0;padding:0;box-sizing:border-box}
html,body{width:1200px;height:675px;overflow:hidden;background:var(--dim)}
.canvas{position:relative;width:1200px;height:675px;overflow:hidden;background:var(--dim);font-family:"Oswald",sans-serif}

.promo-bar{position:absolute;left:0;top:0;width:1200px;height:32px;background:var(--red);color:var(--white)}
.social-btn{position:absolute;top:6px;height:17px;background:var(--fb);color:var(--white);font:700 9.5px/17px "Nunito",sans-serif;border-radius:3px;text-align:center}
.social-like{left:15px;width:74px}
.social-share{left:94px;width:44px}
.promo-line{position:absolute;left:145px;top:0;height:32px;display:flex;align-items:center;gap:9px;white-space:nowrap}
.promo-text{font-size:14px;font-weight:500;letter-spacing:-.35px}
.flag{display:inline-block;flex:none;border-radius:1px}
.flag-ph{width:21px;height:14px;background:linear-gradient(var(--flag-blue) 50%,#d22 50%)}
.currency{position:absolute;left:1065px;top:0;height:32px;font-size:13px;display:flex;align-items:center;gap:4px}
.flag-us{width:20px;height:13px;background:linear-gradient(var(--flag-blue),var(--flag-blue)) 0 0/9px 7px no-repeat,repeating-linear-gradient(#c33 0 2px,#fff 2px 4px)}
.divider{position:absolute;left:1140px;top:8px;width:1px;height:16px;background:rgba(255,255,255,.5)}
.cart{position:absolute;left:1153px;top:6px}
.cart-count{position:absolute;left:1171px;top:1px;width:14px;height:14px;border-radius:50%;background:var(--lime);font:700 8px/14px "Nunito",sans-serif;text-align:center}

.site-header{position:absolute;left:0;top:32px;width:1200px;height:71px;background:var(--white)}
.brand{position:absolute;left:140px;top:27px;display:flex;align-items:center;gap:5px;color:var(--red);font-size:14px;font-weight:500}
.brand-dot{width:12px;height:12px;border-radius:50%;border:2px solid var(--red)}
.search{position:absolute;left:322px;top:17px;width:333px;height:35px;border:1px solid #cfcfcf;display:flex}
.search-field{flex:1;font-size:16px;color:var(--ink);padding:5px 9px;letter-spacing:-.3px}
.search-btn{width:35px;height:33px;background:var(--lime);display:flex;align-items:center;justify-content:center}
.contact{position:absolute;left:990px;top:4px;color:var(--grey-text);font-size:15px;line-height:23px}
.contact-phone{color:var(--lime);font-size:16px;display:flex;align-items:center;gap:6px}
.contact-hours{font-size:13px;line-height:18px}

.main-nav{position:absolute;left:0;top:103px;width:1200px;height:38px;background:var(--nav-bg);border-bottom:2px solid var(--lime);font-size:15px;color:var(--ink)}
.nav-link{position:absolute;top:8px}
.nav-home{left:24px}
.nav-shop{left:75px;display:flex;align-items:center;gap:3px}

.hero{position:absolute;left:16px;top:141px;width:1172px;height:434px;background:linear-gradient(90deg,#3d3a34 0%,#4b4640 35%,#6d6d6a 55%,#7d7b76 100%)}
.heading{position:absolute;left:0;top:622px;width:1200px;text-align:center;font-size:38px;font-weight:500;color:#1f1f1f;letter-spacing:.3px}

.mega-menu{position:absolute;left:9px;top:141px;width:1186px;height:358px;background:var(--white)}
.menu-col{position:absolute;top:20px;font-family:"Nunito",sans-serif}
.menu-col h3{color:var(--red);font-size:14px;font-weight:800;margin-bottom:8px;letter-spacing:.1px}
.menu-col ul{list-style:none}
.menu-col li{color:var(--item);font-size:10.6px;font-weight:800;line-height:15.8px}
.col-coffee{left:37px}
.col-breakfast{left:207px;width:124px}
.col-chai{left:405px}
.col-iced{left:603px}
.col-bev{left:773px;width:128px}
</style>
</head>
<body>
<div class="canvas">
  <div class="hero" role="img" aria-label="Photo of the cafe front with a cream car parked outside and a potted plant"></div>
  <h2 class="heading">YOUR FREE COFFEE AWAITS...</h2>

  <header class="promo-bar">
    <span class="social-btn social-like">Like 6.9K</span>
    <span class="social-btn social-share">Share</span>
    <div class="promo-line">
      <span class="promo-text">Spend $61 USD to Unlock Free Shipping Philippines</span>
      <span class="flag flag-ph" role="img" aria-label="Philippines flag"></span>
    </div>
    <span class="currency"><span class="flag flag-us" role="img" aria-label="US flag"></span>USD
      <svg width="9" height="6" viewBox="0 0 9 6"><path d="M1 1l3.5 3.5L8 1" stroke="#fff" stroke-width="1.6" fill="none"/></svg></span>
    <span class="divider"></span>
    <svg class="cart" width="22" height="20" viewBox="0 0 22 20"><path d="M1 2h3l3 10h11l2-7H6" stroke="#fff" stroke-width="2" fill="none"/><circle cx="8" cy="16" r="2" fill="#fff"/><circle cx="17" cy="16" r="2" fill="#fff"/></svg>
    <span class="cart-count">0</span>
  </header>

  <div class="site-header">
    <div class="brand"><span class="brand-dot"></span>Muga Miles</div>
    <div class="search">
      <span class="search-field">Search...</span>
      <span class="search-btn"><svg width="16" height="16" viewBox="0 0 16 16"><circle cx="6.5" cy="6.5" r="4.7" stroke="#fff" stroke-width="2.2" fill="none"/><path d="M10 10l4.5 4.5" stroke="#fff" stroke-width="2.4"/></svg></span>
    </div>
    <div class="contact">
      <div>Got a Question? Call Us</div>
      <div class="contact-phone"><svg width="15" height="15" viewBox="0 0 16 16"><path d="M3 1l3 3-2 2c1 2 3 4 6 6l2-2 3 3-2 3C7 16 0 9 1 3z" fill="#555"/></svg>0400 123 987</div>
      <div class="contact-hours">Mon-Sat 5.30am-12pm Eastern</div>
    </div>
  </div>

  <nav class="main-nav">
    <span class="nav-link nav-home">HOME</span>
    <span class="nav-link nav-shop">Shop <svg width="9" height="6" viewBox="0 0 9 6"><path d="M1 5l3.5-3.5L8 5" stroke="#333" stroke-width="1.3" fill="none"/></svg></span>
  </nav>

  <div class="mega-menu">
    <div class="menu-col col-coffee">
      <h3>Gourmet Coffee</h3>
      <ul><li>Flat White</li><li>Latte</li><li>Hot Chocolate</li><li>Long Black</li><li>Mocha</li><li>Babyccino</li><li>Macchiato</li><li>Ristretto</li><li>Piccolo Latte</li><li>Espresso</li></ul>
    </div>
    <div class="menu-col col-breakfast">
      <h3>Breakfast</h3>
      <ul><li>Ham, Cheese Croissant</li><li>Bacon &amp; Egg roll</li><li>Thick Raisin Toast x2 Slices</li><li>Brown Bread 2 Slices with spreads</li><li>Mango &amp; Coconut Bread</li><li>Banana Bread</li><li>Gourmet Muffins</li><li>Cheese Toastie with butter</li><li>Turkish Roll</li><li>JUST Bacon Roll</li><li>JUST Egg Roll</li><li>Cheese Croissant</li><li>Plain Croissant</li></ul>
    </div>
    <div class="menu-col col-chai">
      <h3>Chai Latte &amp; Tea</h3>
      <ul><li>Chai Latte</li><li>Dirty Chai Latte</li><li>Filthy Chai</li><li>English Breakfast Tea</li><li>Green Tea</li><li>Peppermint Tea</li><li>Earl Grey</li></ul>
    </div>
    <div class="menu-col col-iced">
      <h3>Iced Drinks</h3>
      <ul><li>Iced Coffee</li><li>Iced Chocolate</li><li>Iced Mocha</li><li>Iced Long Black</li></ul>
    </div>
    <div class="menu-col col-bev">
      <h3>Beverages</h3>
      <ul><li>Water 600ml</li><li>Orange Juice with Pulp 500ml</li><li>Sparkling Mineral Water 330ml</li><li>Ruby Red Smoothie</li><li>Iced Chocolate - Brewhand Co</li><li>Iced Coffee - Brewhand Co</li><li>Volt Energy Drink Bottle</li><li>Kombucha</li></ul>
    </div>
  </div>
</div>
</body>
</html>
```